ecommerce news podcast artwork

Podcast cover art for a podcast featuring daily news and events around ecommerce product businesses.

text to be: VORLA BEAT
optional third line of text with smaller font: Podcast

looking for something that pops with a medium to light blue background. text can be in white/red/orange colors. prefer solid colors for text, but background can vary.
I'm really open to other ideas too, sometimes you don't know what you want until you see it.

Target Market(s)

ecommerce business owners, managers

Industry/Entity Type

news, business, ecommerce

Font styles to use
Sans Serif

Colors
0054AA
0677BA
7BADD7
CADEEF
E8F1F8
0094D4
00A9DD
6FCCEA
C7EBF8
E9F6FB
F0912C
F2A743
F7CA91
FBE8D2
FDF5EE
EB3D1F
EC4F4E
F09395
F8D3D4
FCEDEE

Requirements
Must have
• text: VORLA BEAT
Should not have
• no microphones, headsets/headphones, speakers, or other props like that.

```html
<!DOCTYPE html>
<html lang="en">
<head>
<meta charset="utf-8">
<title>VORLA BEAT Podcast Cover</title>
<link rel="stylesheet" href="https://fonts.googleapis.com/css2?family=Archivo+Black&family=Archivo:wght@700&display=swap">
<style>
  :root {
    --sky-deep: #3f9def;
    --sky-mid: #45c3f7;
    --sky-light: #8fdcf6;
    --glow: #f4fcff;
    --title-red: #e02b1f;
    --title-dark: #292929;
    --label-white: #ffffff;
  }
  html, body {
    margin: 0;
    padding: 0;
    width: 1200px;
    height: 1200px;
    overflow: hidden;
  }
  .cover {
    position: relative;
    width: 1200px;
    height: 1200px;
    overflow: hidden;
    background: radial-gradient(ellipse 46% 44% at 50% 52%, var(--glow) 0%, var(--sky-light) 35%, var(--sky-mid) 68%, var(--sky-deep) 100%);
  }
  .world-backdrop {
    position: absolute;
    inset: 230px 0 160px 0;
    background: radial-gradient(ellipse 70% 60% at 50% 45%, rgba(255,255,255,0) 40%, rgba(70,170,240,0.18) 100%);
  }
  .title {
    position: absolute;
    left: 0;
    width: 100%;
    margin: 0;
    text-align: center;
    font-family: "Archivo Black", "Arial Black", sans-serif;
    font-weight: 400;
    line-height: 1;
    white-space: nowrap;
  }
  .title-top {
    top: 268px;
    font-size: 300px;
    color: var(--title-red);
    letter-spacing: -4px;
  }
  .title-bottom {
    top: 534px;
    font-size: 312px;
    color: var(--title-dark);
    letter-spacing: -2px;
  }
  .label {
    position: absolute;
    top: 846px;
    left: 0;
    width: 100%;
    margin: 0;
    text-align: center;
    font-family: "Archivo", Arial, sans-serif;
    font-weight: 700;
    font-size: 54px;
    line-height: 1;
    letter-spacing: 30px;
    padding-left: 30px;
    box-sizing: border-box;
    color: var(--label-white);
  }
</style>
</head>
<body>
  <main class="cover">
    <div class="world-backdrop" role="img" aria-label="Faint world map with connected network lines"></div>
    <h1 class="title title-top">VORLA</h1>
    <p class="title title-bottom">BEAT</p>
    <p class="label">PODCAST</p>
  </main>
</body>
</html>
```